Quorvex clinic business card - double sided for young clinic

I require business cards for my aesthetic clinic specialising in the below treatments. I would like the cards to be modern as my clinic base are young 22-35 years old. I require my logo on it and would like the edges to be rounded.

I have an aesthetic clinic specialising in :
Quorvex
Lip Enhancement
Chemical Peels
Facial Fillers
Non Surgical Face Lift

I would the cards to have the following information on them:
My logo - (in grey/silver)
address
Phone number
services

Colours :
White/grey/silver and red

a nice image on there, perhaps a set of lips as this is a main service i deliver

Company Name: PDA Address: 52 Farrowmere Road, 4 Brackwell High Street, KT9 4WQ Phone: 0208 794 2160 Website: www.penningtondoweaesthetics.co.uk

Target Market(s)

clinics 22-45 years old mainly female

Industry/Entity Type

Business

Contact Information for Business Card

as above

Requirements
Must have
• logo
• Address
• Email
• Phone number
• Services i offer
Nice to have
• images

```html
<!DOCTYPE html>
<html lang="en">
<head>
<meta charset="utf-8">
<title>Pennington Dowe Aesthetics – Business Card</title>
<link rel="stylesheet" href="https://fonts.googleapis.com/css2?family=Noto+Serif:ital,wght@0,400;0,700;1,700&display=swap">
<style>
  :root {
    --red: #d41215;
    --red-soft: #de4446;
    --white: #ffffff;
    --ink: #2a2a2a;
    --page: #ffffff;
  }
  * { margin: 0; padding: 0; box-sizing: border-box; }
  html, body { width: 960px; height: 1200px; overflow: hidden; background: var(--page); }
  body { position: relative; font-family: "Noto Serif", Georgia, serif; }

  .card { position: absolute; left: 105px; overflow: hidden; box-shadow: 4px 6px 10px rgba(0,0,0,.35); }

  /* front */
  .card-front { top: 156px; width: 750px; height: 430px; background: var(--red); }
  .lips-art { position: absolute; background: var(--red-soft); border-radius: 50%; opacity: .75; }
  .card-front .lips-art { left: 150px; top: 30px; width: 470px; height: 260px; }
  .brand { position: absolute; color: var(--white); text-align: center; }
  .card-front .brand { left: 0; width: 750px; top: 82px; }
  .brand-mark { display: flex; align-items: center; justify-content: center; gap: 12px; font-weight: 700; }
  .brand-mark .dot { width: 16px; height: 16px; border-radius: 50%; background: var(--white); }
  .card-front .brand-mark { font-size: 44px; letter-spacing: 3px; margin-bottom: 30px; }
  .brand-name { letter-spacing: 3px; line-height: 1; }
  .brand-name .line1 { display: block; font-size: 23px; }
  .brand-name .line2 { display: block; font-size: 34px; letter-spacing: 4px; margin-top: 2px; }

  .services { position: absolute; left: 172px; top: 350px; width: 520px; display: grid; grid-template-columns: 253px 1fr; row-gap: 28px; list-style: none; }
  .services li { color: var(--white); font-weight: 700; font-style: italic; font-size: 16.5px; display: flex; align-items: center; gap: 9px; }
  .services li::before { content: "✣"; font-style: normal; font-size: 13px; }

  /* back */
  .card-back { top: 606px; width: 765px; height: 438px; background: var(--white); }
  .side-panel { position: absolute; left: 0; top: 0; width: 222px; height: 100%; background: var(--red); }
  .side-panel .lips-art { left: 6px; top: 16px; width: 210px; height: 210px; transform: rotate(-40deg); border-radius: 50% / 40%; }
  .side-panel .brand { left: 0; width: 222px; top: 265px; }
  .side-panel .brand-mark { font-size: 32px; letter-spacing: 2px; margin-bottom: 28px; }
  .side-panel .brand-mark .dot { width: 12px; height: 12px; }
  .side-panel .brand-name .line1 { font-size: 17px; letter-spacing: 2px; }
  .side-panel .brand-name .line2 { font-size: 24px; letter-spacing: 3px; }

  .holder { position: absolute; right: 38px; top: 42px; text-align: right; }
  .holder-name { font-size: 33px; font-weight: 700; font-style: italic; color: var(--ink); line-height: 1; }
  .holder-role { font-size: 14px; font-weight: 700; font-style: italic; color: var(--red); margin-top: 2px; margin-right: 22px; }

  .contact { position: absolute; right: 38px; top: 192px; list-style: none; }
  .contact li { display: flex; align-items: center; justify-content: flex-end; gap: 10px; height: 54px; font-size: 24px; color: var(--ink); }
  .contact svg { width: 36px; height: 36px; flex: none; }
</style>
</head>
<body>

<section class="card card-front">
  <div class="lips-art" role="img" aria-label="Faint lip print illustration"></div>
  <div class="brand">
    <div class="brand-mark"><span class="dot"></span>PDA</div>
    <div class="brand-name"><span class="line1">PENNINGTON DOWE</span><span class="line2">AESTHETICS</span></div>
  </div>
  <ul class="services">
    <li>Chemical Peel</li>
    <li>Wrinkle Relaxing Injections</li>
    <li>Cosmetic Surgery</li>
    <li>Dermal Fillers</li>
  </ul>
</section>

<section class="card card-back">
  <div class="side-panel">
    <div class="lips-art" role="img" aria-label="Faint lip print illustration"></div>
    <div class="brand">
      <div class="brand-mark"><span class="dot"></span>PDA</div>
      <div class="brand-name"><span class="line1">PENNINGTON DOWE</span><span class="line2">AESTHETICS</span></div>
    </div>
  </div>

  <div class="holder">
    <div class="holder-name">Maren Pennington</div>
    <div class="holder-role">OWNER</div>
  </div>

  <ul class="contact">
    <li>020 8794 2160
      <svg viewBox="0 0 24 24" fill="none" stroke="var(--red)" stroke-width="2" stroke-linecap="round"><path d="M6 3l3 4-2 2c1 3 3 5 6 6l2-2 4 3-2 3C10 19 5 14 3 6z" fill="var(--red)"/><path d="M14 6a5 5 0 0 1 4 4M15 2a9 9 0 0 1 7 7"/></svg>
    </li>
    <li>4 Brackwell Parade, Surrey, KT9 4WQ
      <svg viewBox="0 0 24 24" fill="none" stroke="var(--red)" stroke-width="2"><path d="M12 21s-6-7-6-11a6 6 0 0 1 12 0c0 4-6 11-6 11z" fill="var(--red)"/><circle cx="12" cy="10" r="2.2" fill="var(--white)" stroke="none"/><ellipse cx="12" cy="21.5" rx="6" ry="1.5"/></svg>
    </li>
    <li>pdabrackwellbookings@mailbox.co.uk
      <svg viewBox="0 0 24 24" fill="none" stroke="var(--red)" stroke-width="1.6"><rect x="2" y="9" width="20" height="13"/><path d="M2 9l10 7 10-7M5 11V4h14v7"/><circle cx="12" cy="8" r="2"/></svg>
    </li>
    <li>www.penningtondoweaesthetics.co.uk
      <svg viewBox="0 0 24 24" fill="none" stroke="var(--red)" stroke-width="1.6"><circle cx="12" cy="12" r="10"/><ellipse cx="12" cy="12" rx="4.5" ry="10"/><path d="M2 12h20M4 7h16M4 17h16"/></svg>
    </li>
  </ul>
</section>

</body>
</html>
```